Real Estate Virtual 360 Tour Web Home Page [Design Only]

see new upload mockup attached

We want new design ideas for our home page.

Link to video from web dev team of wireframe for reference: https://files.quorvantshare.net/d/7q-WpR2n8Lx4Tb6Hc0Yv9Ke3Mz5Ud/view?usp=sharing

Things desired on the home page:

Book a shoot now - Multiple markets,links to the corresponding market page for actual booking

1 Complete Package - includes Video, 3D Doviquell Tours, Exterior 360 Tours, Map, Agent Profile, Floor Plans, 2D Photos with blue sky and twilight sky guarantee

How it Works-https://clipnestra.net/582716049

Pricing-https://brisklumehomes.net/pricing/

House Search-https://brisklumehomes.net/

Footer
Updates

Target Market(s)

Real Estate Agents, Realtors, Home Buyers

Number of Pages Required

1 page

Font styles to use
Sans Serif

Colors
0555a3

Requirements
Must have
• see new upload mockup attached

Footer

```html
<!DOCTYPE html>
<html lang="en">
<head>
<meta charset="utf-8">
<title>Brisklume Homes – Virtual Reality Listings</title>
<link href="https://fonts.googleapis.com/css2?family=Montserrat:wght@400;500;600;700&display=swap" rel="stylesheet">
<style>
:root{
  --teal:#00b094;
  --teal-dark:#1d7d72;
  --teal-hero:#2f8c82;
  --mint:#a9e0d6;
  --mint-soft:#d6efea;
  --mint-card:#c9ece5;
  --orange:#e24a1a;
  --bg:#f3f3f3;
  --ink:#1e1e1e;
  --ink-soft:#333;
  --white:#fff;
  --grey:#9a9a9a;
}
*{box-sizing:border-box;margin:0;padding:0}
html,body{width:1200px;height:3750px;overflow:hidden}
body{font-family:'Montserrat',sans-serif;background:var(--bg);color:var(--ink);position:relative}
.abs{position:absolute}
.btn{position:absolute;display:flex;align-items:center;justify-content:center;font-weight:700;font-size:14px;letter-spacing:.3px;text-transform:uppercase}
.btn-fill{background:var(--orange);color:var(--white)}
.btn-line{border:2px solid var(--orange);color:var(--orange);background:transparent}

/* top bar + hero */
.topbar{top:0;left:0;width:1200px;height:29px;background:var(--teal-dark);z-index:3}
.topbar .phone{position:absolute;left:150px;top:8px;font-size:10px;color:var(--white);font-weight:500}
.topbar .social{position:absolute;top:5px;width:19px;height:19px;border-radius:50%;background:rgba(255,255,255,.55)}
.hero{top:29px;left:0;width:1200px;height:525px;background:linear-gradient(160deg,#5c9d95 0%,#3f8a80 45%,#2b6f66 100%)}
.hero-shade{top:29px;left:0;width:1200px;height:525px;background:rgba(37,128,117,.35)}
.brand{left:150px;top:42px;width:70px;color:var(--white);font-weight:600;font-size:14px;line-height:15px;letter-spacing:.5px;z-index:3}
.nav{top:57px;right:150px;display:flex;gap:34px;font-size:12px;font-weight:500;color:var(--white);z-index:3}
.nav .on{color:var(--orange)}
.hero-title{top:176px;left:0;width:1200px;text-align:center;color:var(--white);font-size:35px;font-weight:700;letter-spacing:.3px}
.hero-sub{top:243px;left:0;width:1200px;text-align:center;color:var(--white);font-size:15px;line-height:23px}

/* blobs */
.blob{position:absolute;fill:var(--mint)}

/* packages */
.h2{position:absolute;font-size:24px;font-weight:700;color:var(--ink)}
.features{left:155px;top:718px;width:450px;list-style:none;font-size:12.5px;font-weight:500;color:var(--ink-soft)}
.features li{position:relative;padding-left:25px;line-height:14px;margin-bottom:12px}
.features li::before{content:"";position:absolute;left:2px;top:4px;width:7px;height:7px;border-radius:50%;background:var(--teal)}
.features li span{display:block;padding-left:7px}
.collage{position:absolute;box-shadow:0 4px 16px rgba(0,0,0,.12)}

/* steps */
.step-circle{position:absolute;width:300px;height:300px;border-radius:50%;background:var(--mint-soft)}
.step-title{position:absolute;font-size:16px;font-weight:700}
.step-text{position:absolute;width:300px;font-size:15px;line-height:27px;color:var(--ink-soft)}
.learn{position:absolute;font-size:13px;font-weight:700;color:var(--orange)}

/* pricing */
.pricing{top:2092px;left:0;width:1200px;height:692px;background:var(--teal);overflow:hidden}
.pricing-title{top:2180px;left:0;width:1200px;text-align:center;color:var(--white);font-size:24px;font-weight:700}
.card{position:absolute;top:2260px;width:214px;height:436px;background:var(--bg);border-radius:10px;overflow:hidden;text-align:center}
.card-head{height:43px;background:var(--orange);color:var(--white);font-size:9px;font-weight:700;line-height:43px}
.card-name{position:relative;margin:19px 0 0;height:40px;display:flex;flex-direction:column;justify-content:center;font-size:15px;font-weight:700}
.card-name small{font-size:10px;font-weight:600}
.card-name .arr{position:absolute;top:10px;width:10px;height:16px}
.price{margin-top:18px;font-size:44px;font-weight:700;line-height:50px}
.price sup{font-size:28px;vertical-align:-4px}
.dur{margin-top:12px;font-size:12px;font-weight:500}
.desc{margin:52px auto 0;width:190px;font-size:12.5px;line-height:18px;color:var(--ink-soft);height:90px}
.book{position:absolute;left:47px;bottom:30px;width:120px;height:30px;background:var(--orange);color:var(--white);font-size:9px;font-weight:700;line-height:30px}

/* search */
.filters{top:2930px;left:150px;width:900px;height:134px;background:var(--mint-soft)}
.field{position:absolute;background:var(--white);border:1px solid #d8e6e3;height:36px;font-size:13px;color:#777;padding:0 14px;display:flex;align-items:center;justify-content:space-between}
.field b{font-size:9px;color:#444}
.check{position:absolute;display:flex;align-items:center;gap:14px;font-size:14px;font-weight:600;color:#555}
.check i{display:block;width:16px;height:16px;background:var(--white);border:1px solid #c9c9c9}
.listing{position:absolute;top:3094px;width:286px;height:236px;background:var(--mint-card)}
.listing-head{height:22px;background:var(--teal);color:var(--white);font-size:11px;font-weight:700;display:flex;justify-content:space-between;padding:4px 22px 0}
.listing-photo{height:117px}
.listing-addr{padding:15px 15px 0;font-size:12px;font-weight:600;line-height:13px;height:40px}
.listing-meta{padding:4px 15px;display:flex;gap:18px;font-size:10px;font-weight:500}
.pager{top:3352px;left:520px;display:flex;gap:2px;align-items:flex-end}
.pager span{background:#bfbfbf;color:var(--white);font-size:9px;font-weight:700;padding:2px 4px}
.pager .cur{background:var(--teal);font-size:11px;padding:3px 7px}
.map{top:3381px;left:150px;width:900px;height:303px;background:linear-gradient(135deg,#d9ead0 0%,#e8efe0 45%,#f1f0e6 70%,#e3ecd9 100%)}
.map-tabs{top:3394px;left:155px;display:flex;background:var(--white);font-size:9px;box-shadow:0 1px 3px rgba(0,0,0,.2)}
.map-tabs span{padding:5px 11px}
.footer{top:3722px;left:0;width:1200px;height:28px;background:var(--teal-dark);color:var(--white);font-size:9px;font-weight:600}
</style>
</head>
<body>

<!-- header -->
<div class="abs hero" role="img" aria-label="Bright modern kitchen interior with island counter and plants"></div>
<div class="abs hero-shade"></div>
<div class="abs topbar">
  <div class="phone">Call: (+1) 555 214 0386</div>
  <span class="social" style="left:968px"></span>
  <span class="social" style="left:999px"></span>
  <span class="social" style="left:1030px"></span>
</div>
<div class="abs brand">BRISKLUME HOMES</div>
<nav class="abs nav">
  <span class="on">HOME</span><span>COMERCIAL</span><span>PRICING</span><span>SERVICES</span><span>PROPERTIES</span><span>CAREER OPPORTUNITIES</span>
</nav>
<h1 class="abs hero-title">WIN THE LISTINGS WITH VIRTUAL REALITY</h1>
<p class="abs hero-sub">We offer one complete package, for any type of real estate<br>to have the best possible property display</p>
<a class="btn btn-fill" style="left:495px;top:338px;width:210px;height:51px">Schedule a shoot</a>

<!-- decorative blobs -->
<svg class="blob" style="left:1140px;top:580px" width="60" height="240" viewBox="0 0 60 240"><path d="M60 0 C20 10 0 50 5 100 C10 160 40 210 60 240 Z"/></svg>
<svg class="blob" style="left:0;top:935px" width="58" height="230" viewBox="0 0 58 230"><path d="M0 0 C40 5 60 50 55 100 C50 150 20 200 0 230 Z"/></svg>
<svg class="blob" style="left:1050px;top:1395px" width="150" height="240" viewBox="0 0 150 240"><path d="M150 0 C100 10 60 50 30 110 C0 170 20 230 90 235 L150 240 Z"/></svg>
<svg class="blob" style="left:0;top:1735px" width="60" height="250" viewBox="0 0 60 250"><path d="M0 0 C40 10 60 70 58 130 C56 190 35 235 0 250 Z"/></svg>

<!-- packages -->
<h2 class="h2" style="left:150px;top:638px">WHATS INCLUDED INSIDE PACKAGES?</h2>
<ul class="abs features">
  <li>90 Second Drone Marketing Video in 4K</li>
  <li>Internal Doviquell 3D Virtual Tour 4K</li>
  <li>HD HDR 2D MLS Ready Photos<span>20-50 stills based on layout of the house</span></li>
  <li>360 Panoramas of the exterior and from the Sky 4K<span>Featuring Annotations of Local Schools and Attractions from 200ft above the property</span></li>
  <li>HDR Cover Photo from Drone 4K</li>
  <li>CAD Schematic Floor Plans</li>
  <li>Project Specific URL Landing Page Marketed specifically to you<span>and your brokerage</span></li>
  <li>Property Specific QR Code and Shortened URL (Brisk.Tours/xyz)</li>
</ul>
<div class="collage" style="left:790px;top:645px;width:238px;height:150px;background:linear-gradient(135deg,#e9e2d6,#c9b79b)" role="img" aria-label="Sunlit living room interior"></div>
<div class="collage" style="left:870px;top:795px;width:180px;height:150px;background:linear-gradient(135deg,#7c8f62,#b66a4a 55%,#8a9b72)" role="img" aria-label="Aerial view of neighbourhood rooftops"></div>
<div class="collage" style="left:710px;top:873px;width:160px;height:100px;background:#fff" role="img" aria-label="Floor plan drawing"></div>
<div class="collage" style="left:623px;top:695px;width:247px;height:178px;background:linear-gradient(180deg,#aac3d8,#dfe8ef)" role="img" aria-label="Camera drone in flight"></div>
<a class="btn btn-fill" style="left:371px;top:1026px;width:210px;height:53px">Schedule a shoot</a>
<a class="btn btn-line" style="left:619px;top:1026px;width:210px;height:53px">View full package</a>

<!-- how -->
<h2 class="h2" style="left:0;width:1200px;text-align:center;top:1166px">HOW WILL WE GET IT DONE</h2>
<div class="step-circle" style="left:224px;top:1245px" role="img" aria-label="Website layout illustration"></div>
<div class="step-title" style="left:674px;top:1280px">Create your specialized website</div>
<p class="step-text" style="left:674px;top:1320px">We start off by building you a beautiful website for all of your digital assets We give you a shortened URL You can drop it into the MLS virtual tours and it can syndicate out to all of the major listing sites.</p>
<span class="learn" style="left:674px;top:1495px">LEARN MORE</span>

<div class="step-title" style="left:224px;top:1618px">Ready up your assets</div>
<p class="step-text" style="left:224px;top:1657px">we are going to have a 90-second drone video. We're going to have a virtual reality walking tour of the inside of the property, that also has a 3d model that spins around allowing you to drop back into the house wherever you want to and much more .</p>
<span class="learn" style="left:225px;top:1862px">LEARN MORE</span>
<div class="step-circle" style="left:674px;top:1597px" role="img" aria-label="Drone illustration"></div>

<a class="btn btn-fill" style="left:371px;top:1951px;width:210px;height:53px">Schedule a shoot</a>
<a class="btn btn-line" style="left:619px;top:1951px;width:210px;height:53px">Learn more</a>

<!-- pricing -->
<section class="abs pricing">
  <svg class="abs" style="left:0;top:0" width="1200" height="692" viewBox="0 0 1200 692">
    <path d="M0 0 H350 C380 80 300 140 200 150 C120 160 40 130 0 100 Z" fill="#2ec2ab"/>
    <path d="M820 150 C850 90 980 80 1040 120 C1100 160 1060 220 960 230 C880 236 800 210 820 150 Z" fill="#2ec2ab"/>
    <path d="M330 692 C350 600 500 580 580 610 C660 640 650 692 650 692 Z" fill="#2ec2ab"/>
  </svg>
</section>
<h2 class="abs pricing-title">PRICING</h2>

<div class="card" style="left:150px">
  <div class="card-head">INTRODUCTION SERVICES</div>
  <div class="card-name"><svg class="arr" style="left:18px" viewBox="0 0 10 16"><path d="M8 2 L2 8 L8 14" stroke="#e24a1a" stroke-width="3" fill="none"/></svg>PRESENTATION<svg class="arr" style="right:18px" viewBox="0 0 10 16"><path d="M2 2 L8 8 L2 14" stroke="#e24a1a" stroke-width="3" fill="none"/></svg></div>
  <div class="price">FREE</div>
  <div class="dur">1 HOUR</div>
  <p class="desc">Presenting Our Product in front of group or attendees, sponsoring breakfast or lunch for the purpose of educating and marketing.</p>
  <div class="book">BOOK SERVICE</div>
</div>
<div class="card" style="left:379px">
  <div class="card-head">BRISKLUME TOUR</div>
  <div class="card-name"><svg class="arr" style="left:18px" viewBox="0 0 10 16"><path d="M8 2 L2 8 L8 14" stroke="#e24a1a" stroke-width="3" fill="none"/></svg><span>1100 <small>sqft or less</small></span><small>Full Package</small><svg class="arr" style="right:18px" viewBox="0 0 10 16"><path d="M2 2 L8 8 L2 14" stroke="#e24a1a" stroke-width="3" fill="none"/></svg></div>
  <div class="price"><sup>$</sup>249</div>
  <div class="dur">3 HOURS</div>
  <p class="desc">acreage on houses are an additional <b>$100</b> per 25 acre block and is applied after 1 acre</p>
  <div class="book">BOOK SERVICE</div>
</div>
<div class="card" style="left:607px">
  <div class="card-head">LAND PACKAGES</div>
  <div class="card-name"><svg class="arr" style="left:18px" viewBox="0 0 10 16"><path d="M8 2 L2 8 L8 14" stroke="#e24a1a" stroke-width="3" fill="none"/></svg><span>10-25 <small>acres</small></span><small>Full Package</small><svg class="arr" style="right:18px" viewBox="0 0 10 16"><path d="M2 2 L8 8 L2 14" stroke="#e24a1a" stroke-width="3" fill="none"/></svg></div>
  <div class="price"><sup>$</sup>279</div>
  <div class="dur">3 HOURS 30 MIN</div>
  <p class="desc">Lorem ipsum dolor sit amet, consectetur adipisicing elit, sed do eiusmod tempor incididunt ut labore et dolore magna aliqua. Ut enim ad</p>
  <div class="book">BOOK SERVICE</div>
</div>
<div class="card" style="left:836px">
  <div class="card-head">COMMERCIAL</div>
  <div class="card-name"><svg class="arr" style="left:18px" viewBox="0 0 10 16"><path d="M8 2 L2 8 L8 14" stroke="#e24a1a" stroke-width="3" fill="none"/></svg><span>REGULAR</span><small>10,000⁺ sqft property</small><svg class="arr" style="right:18px" viewBox="0 0 10 16"><path d="M2 2 L8 8 L2 14" stroke="#e24a1a" stroke-width="3" fill="none"/></svg></div>
  <div class="price"><sup>$</sup>140</div>
  <div class="dur">2⁺ HOUR</div>
  <p class="desc">$140 per 1,000 total sqft, + $50 per separate unit (volume discounts available).</p>
  <div class="book">BOOK SERVICE</div>
</div>

<!-- search -->
<h2 class="h2" style="left:0;width:1200px;text-align:center;top:2870px">FIND HOUSES USING OUR SERVICES</h2>
<div class="abs filters">
  <div class="field" style="left:22px;top:22px;width:182px">Select city <svg width="12" height="8" viewBox="0 0 12 8"><path d="M1 1 L6 6 L11 1" stroke="#444" stroke-width="1.6" fill="none"/></svg></div>
  <div class="field" style="left:22px;top:75px;width:182px">Select type <svg width="12" height="8" viewBox="0 0 12 8"><path d="M1 1 L6 6 L11 1" stroke="#444" stroke-width="1.6" fill="none"/></svg></div>
  <div class="field" style="left:225px;top:22px;width:166px">Min price <b>USD</b></div>
  <div class="field" style="left:225px;top:75px;width:166px">Max price <b>USD</b></div>
  <div class="field" style="left:412px;top:22px;width:151px">Min bedrooms</div>
  <div class="field" style="left:412px;top:75px;width:151px">Min Bathrooms</div>
  <div class="check" style="left:583px;top:32px"><i></i>Basement</div>
  <div class="check" style="left:583px;top:85px"><i></i>Garage</div>
  <div class="field" style="left:707px;top:22px;width:70px">20</div>
  <div class="field" style="left:787px;top:22px;width:48px;padding:0 8px">Mi <svg width="12" height="8" viewBox="0 0 12 8"><path d="M1 1 L6 6 L11 1" stroke="#444" stroke-width="1.6" fill="none"/></svg></div>
  <div class="check" style="left:850px;top:32px;font-size:13px">From</div>
  <div class="field" style="left:707px;top:75px;width:175px;padding-right:0">Choose location <span style="width:32px;height:34px;background:var(--orange);display:flex;align-items:center;justify-content:center"><svg width="12" height="16" viewBox="0 0 12 16"><path d="M6 15 C2 10 1 8 1 6 A5 5 0 0 1 11 6 C11 8 10 10 6 15 Z" fill="#fff"/><circle cx="6" cy="6" r="2" fill="#e24a1a"/></svg></span></div>
</div>

<div class="listing" style="left:150px">
  <div class="listing-head"><span>FOR SALE</span><span>$295000</span></div>
  <div class="listing-photo" role="img" aria-label="Single storey house with driveway" style="background:linear-gradient(180deg,#8fb0d6,#b9b5ac 55%,#7c7468)"></div>
  <div class="listing-addr">4120 Alder Crest Rd Pinehollow,<br>CO 80991</div>
  <div class="listing-meta"><span>Beds: 2</span><span>Baths: 1</span><span>859 sqft</span></div>
</div>
<div class="listing" style="left:457px">
  <div class="listing-head"><span>FOR SALE</span><span>$326000</span></div>
  <div class="listing-photo" role="img" aria-label="Two storey house among snowy trees" style="background:linear-gradient(180deg,#5f6e66,#8da0a4 50%,#d9dde0)"></div>
  <div class="listing-addr">227 Quarry Ridge Ln Westvale, CO 80974</div>
  <div class="listing-meta"><span>Beds: 3</span><span>Baths: 2</span><span>960 sqft</span></div>
</div>
<div class="listing" style="left:764px">
  <div class="listing-head"><span>FOR SALE</span><span>$434900</span></div>
  <div class="listing-photo" role="img" aria-label="Suburban house with garage" style="background:linear-gradient(180deg,#cfd8e2,#a99886 55%,#e6e4e0)"></div>
  <div class="listing-addr">9310 Larkspur Ct Mesa Glen, CO 80962</div>
  <div class="listing-meta"><span>Beds: 3</span><span>Baths: 3</span><span>1856 sqft</span></div>
</div>

<div class="abs pager"><span>Back</span><span class="cur">1</span><span>2</span><span>3</span><span>4</span><span>...</span><span>Next</span></div>

<div class="abs map" role="img" aria-label="Map of listing locations"></div>
<div class="abs map-tabs"><span style="font-weight:600">Map</span><span style="color:#666">Satellite</span></div>

<footer class="abs footer">
  <span class="abs" style="left:150px;top:9px">Copyright © 2020 Brisklume Homes All rights reserved.</span>
  <span class="abs" style="right:150px;top:9px">Privacy policy &nbsp;|&nbsp; Terms &amp; conditions &nbsp;|&nbsp; Support</span>
</footer>

</body>
</html>
```